Lantern Motion for Neighbors Business Cards

I need business cards for staff in a new startup. Our company name is Movrela - we train Tai Chi teachers. But our biggest project is called Lantern Motion for Neighbors - a federal project to put together free Tai Chi classes for Vets all across America. It's a young company, with a spirit of excitement, passion, a desire to do good for others (our Vets) and a modern style and sensibility. In other words, not old-fashioned Asian martial arts theme, but something new.

Industry/Entity Type

Health And Wellness

Contact Information for Business Card

The topic is ancient healing, but the company is the Pembrooks - so I'd like a card design that captures that.

Font styles to use
Sans Serif

Colors

Designer to choose colors to be used in the design.

Requirements
Nice to have
• I've got two logos - one for the company and one for the project. I want to see if we can incorporate them both without it becoming too busy.
Should not have
• Overly old-fashioned yin-yang themes.

```html
<!DOCTYPE html>
<html lang="en">
<head>
<meta charset="utf-8">
<title>Lantern Motion for Neighbors – Business Cards</title>
<link rel="stylesheet" href="https://fonts.googleapis.com/css2?family=Lato:wght@400;700;900&display=swap">
<style>
  :root {
    --backdrop: #5e4330;
    --card-white: #ffffff;
    --brand-purple: #3f3b7c;
    --brand-red: #e8344a;
    --wave-pink: #f39ca1;
    --text-grey: #3d3d3d;
    --text-light: #ffffff;
  }
  * { margin: 0; padding: 0; box-sizing: border-box; }
  html, body {
    width: 1200px;
    height: 1023px;
    overflow: hidden;
    background: var(--backdrop);
    font-family: "Lato", Arial, sans-serif;
  }
  .card {
    position: absolute;
    left: 248px;
    width: 681px;
    height: 389px;
    overflow: hidden;
    box-shadow: -6px 6px 0 rgba(63, 59, 124, 0.85), -8px 10px 14px rgba(0, 0, 0, 0.45);
  }
  .card--front { top: 87px; background: var(--card-white); }
  .card--back { top: 541px; background: var(--brand-purple); }

  .front-waves { position: absolute; inset: 0; width: 681px; height: 389px; }

  .company-mark {
    position: absolute;
    left: 62px;
    top: 90px;
    display: flex;
    align-items: center;
    gap: 14px;
  }
  .company-mark__dot {
    width: 52px; height: 52px;
    border-radius: 50%;
    background: var(--brand-red);
  }
  .company-mark__name {
    font-weight: 900;
    font-size: 34px;
    color: var(--brand-red);
    letter-spacing: 0.5px;
  }

  .person {
    position: absolute;
    right: 27px;
    top: 38px;
    text-align: right;
  }
  .person__name {
    font-weight: 900;
    font-size: 37px;
    line-height: 1;
    color: var(--brand-red);
    letter-spacing: 0.3px;
  }
  .person__title {
    margin-top: 10px;
    font-size: 18px;
    color: var(--text-grey);
  }

  .address {
    position: absolute;
    right: 27px;
    top: 216px;
    text-align: right;
    font-size: 18px;
    line-height: 24px;
    color: var(--text-light);
  }
  .contact-list {
    position: absolute;
    right: 27px;
    top: 277px;
    list-style: none;
    text-align: right;
    color: var(--text-light);
    font-size: 18px;
  }
  .contact-list li {
    display: flex;
    justify-content: flex-end;
    align-items: center;
    gap: 10px;
    height: 31px;
  }
  .contact-list svg { width: 18px; height: 18px; flex: none; }

  .project-mark {
    position: absolute;
    left: 120px;
    top: 126px;
    display: flex;
    align-items: center;
    gap: 34px;
  }
  .project-mark__ring {
    width: 136px; height: 136px;
    border-radius: 50%;
    border: 3px solid var(--text-light);
  }
  .project-mark__name {
    color: var(--text-light);
    font-weight: 700;
    font-size: 36px;
    line-height: 1;
    letter-spacing: 0.5px;
  }
  .project-mark__name span {
    display: block;
    margin-top: 8px;
    font-size: 36px;
  }
</style>
</head>
<body>

<section class="card card--front" aria-label="Business card front">
  <svg class="front-waves" viewBox="0 0 1135 648" preserveAspectRatio="none" aria-hidden="true">
    <path fill="var(--wave-pink)" d="M0,360 C120,470 300,520 480,435 C650,355 820,290 975,297 C820,312 650,405 480,492 C300,575 110,530 0,440 Z"/>
    <path fill="var(--brand-purple)" d="M0,470 C150,545 320,575 500,480 C660,395 800,315 950,312 C1050,312 1110,340 1135,362 L1135,648 L0,648 Z"/>
  </svg>

  <div class="company-mark">
    <div class="company-mark__dot"></div>
    <div class="company-mark__name">Movrela</div>
  </div>

  <div class="person">
    <div class="person__name">ADRIAN VALE</div>
    <div class="person__title">Managing Director</div>
  </div>

  <div class="address">
    2345 First Address Line<br>
    Second Address Line, 56324
  </div>

  <ul class="contact-list">
    <li>123 456 7890
      <svg viewBox="0 0 24 24" fill="none" stroke="currentColor" stroke-width="2" stroke-linecap="round" stroke-linejoin="round"><path d="M22 16.9v3a2 2 0 0 1-2.2 2 19.8 19.8 0 0 1-8.6-3.1 19.5 19.5 0 0 1-6-6A19.8 19.8 0 0 1 2.1 4.2 2 2 0 0 1 4.1 2h3a2 2 0 0 1 2 1.7c.1.9.4 1.8.7 2.7a2 2 0 0 1-.5 2.1L8 9.8a16 16 0 0 0 6 6l1.3-1.3a2 2 0 0 1 2.1-.4c.9.3 1.8.6 2.7.7a2 2 0 0 1 1.9 2z"/></svg>
    </li>
    <li>lorem@yourwebsite.com
      <svg viewBox="0 0 24 24" fill="none" stroke="currentColor" stroke-width="2" stroke-linejoin="round"><rect x="2" y="5" width="20" height="14"/><path d="M2 5l10 8 10-8M2 19l7-7M22 19l-7-7"/></svg>
    </li>
    <li>www.yourwebsite.com
      <svg viewBox="0 0 24 24" fill="none" stroke="currentColor" stroke-width="1.8"><circle cx="12" cy="12" r="10"/><path d="M2 12h20M12 2a15 15 0 0 1 0 20M12 2a15 15 0 0 0 0 20"/></svg>
    </li>
  </ul>
</section>

<section class="card card--back" aria-label="Business card back">
  <div class="project-mark">
    <div class="project-mark__ring"></div>
    <div class="project-mark__name">LANTERN MOTION<span>FOR NEIGHBORS</span></div>
  </div>
</section>

</body>
</html>
```